Business Card Design Project

I need a business card for a Management Consultancy. We work with organisational design and development and strategic change using facilitation, consulting and coaching.

Size of card is 90 x 55mm.

Logo is attached.

Wording is:

Carla Brennick
Director

tel 0417286194
email is: info@bluepathvista.com.au

Target Market(s)

Government departments and not for profit organisations mainly.

Industry/Entity Type

Business

Requirements
Must have
• White or colour background not black.

On one side of the card, either back or front please include the words:

Leading Strategic Change

Two sided business card

```html
<!DOCTYPE html>
<html lang="en">
<head>
<meta charset="utf-8">
<title>BluePath Vista – Business Cards</title>
<link rel="stylesheet" href="https://fonts.googleapis.com/css2?family=Open+Sans:wght@400;600;700&display=swap">
<style>
  :root {
    --navy: #1f3d5c;
    --green: #6fa83a;
    --card: #f7f7f7;
    --ink-light: #e6edf3;
    --rule: #9aa4ad;
    --stage: #3a3a3c;
  }
  * { box-sizing: border-box; margin: 0; padding: 0; }
  html, body { width: 1200px; height: 900px; overflow: hidden; }
  body {
    background: var(--stage);
    font-family: "Open Sans", Arial, sans-serif;
    position: relative;
  }
  .card {
    position: absolute;
    width: 540px;
    height: 330px;
    background: var(--card);
    overflow: hidden;
    box-shadow: 0 10px 24px rgba(0,0,0,0.45);
  }
  .card--back { left: 40px; top: 285px; }
  .card--front { left: 620px; top: 285px; }

  .card__shapes { position: absolute; inset: 0; }

  /* logo block */
  .brand { position: absolute; display: flex; align-items: center; }
  .brand__mark { border-radius: 50%; background: var(--navy); flex: none; }
  .brand__text { display: flex; flex-direction: column; align-items: center; }
  .brand__name { font-weight: 700; color: var(--navy); white-space: nowrap; line-height: 1.1; }
  .brand__tagline {
    color: var(--green);
    font-weight: 600;
    white-space: nowrap;
    border-top: 1px solid var(--rule);
    text-transform: lowercase;
  }

  .card--back .brand { left: 32px; top: 38px; gap: 12px; }
  .card--back .brand__mark { width: 42px; height: 42px; }
  .card--back .brand__name { font-size: 24px; }
  .card--back .brand__tagline {
    font-size: 8.5px; letter-spacing: 2.2px; margin-top: 2px; padding-top: 1px;
  }

  .card--front .brand {
    left: 0; width: 440px; top: 56px;
    flex-direction: column; gap: 14px;
  }
  .card--front .brand__mark { width: 84px; height: 84px; }
  .card--front .brand__name { font-size: 44px; letter-spacing: -0.5px; }
  .card--front .brand__tagline {
    font-size: 14px; letter-spacing: 5px; margin-top: 6px; padding-top: 6px;
  }

  /* contact details */
  .contact {
    position: absolute;
    color: var(--ink-light);
    font-size: 13.5px;
    line-height: 1.45;
  }
  .contact--person { left: 34px; bottom: 22px; }
  .contact--office { left: 310px; top: 170px; }
  .contact--office .contact__line--indent { padding-left: 64px; }

  .web-vertical {
    position: absolute;
    right: 0; top: 0;
    width: 84px; height: 330px;
    display: flex; align-items: center; justify-content: center;
    color: var(--ink-light);
    font-size: 14px;
    letter-spacing: 0.5px;
    writing-mode: vertical-rl;
  }
</style>
</head>
<body>

  <section class="card card--back" aria-label="Business card, contact side">
    <svg class="card__shapes" viewBox="0 0 540 330" aria-hidden="true">
      <polygon points="0,190 190,190 190,160 540,160 540,330 0,330" fill="var(--navy)"/>
      <rect x="0" y="184" width="190" height="3" fill="var(--green)"/>
      <rect x="190" y="154" width="240" height="3" fill="var(--navy)"/>
      <rect x="430" y="154" width="110" height="3" fill="var(--green)"/>
      <rect x="190" y="160" width="3" height="30" fill="var(--navy)"/>
    </svg>

    <div class="brand">
      <span class="brand__mark"></span>
      <div class="brand__text">
        <span class="brand__name">BluePath Vista</span>
        <span class="brand__tagline">Leading Strategic Change</span>
      </div>
    </div>

    <div class="contact contact--office">
      <p class="contact__line">Web: www.bluepathvista.com</p>
      <p class="contact__line">Address: 118 Harlow Creek Road</p>
      <p class="contact__line contact__line--indent">Easton CT 06612</p>
    </div>

    <div class="contact contact--person">
      <p class="contact__line">Name: Carla Brennick, Director</p>
      <p class="contact__line">E-mail: info@bluepathvista.com.au</p>
      <p class="contact__line">Phone Nr.: 0417286194</p>
    </div>
  </section>

  <section class="card card--front" aria-label="Business card, logo side">
    <svg class="card__shapes" viewBox="0 0 540 330" aria-hidden="true">
      <rect x="456" y="0" width="84" height="330" fill="var(--navy)"/>
      <rect x="440" y="0" width="3" height="60" fill="var(--green)"/>
      <rect x="440" y="60" width="3" height="210" fill="var(--navy)"/>
      <rect x="440" y="270" width="3" height="60" fill="var(--green)"/>
    </svg>

    <div class="brand">
      <span class="brand__mark"></span>
      <div class="brand__text">
        <span class="brand__name">BluePath Vista</span>
        <span class="brand__tagline">Leading Strategic Change</span>
      </div>
    </div>

    <p class="web-vertical">www.bluepathvista.com</p>
  </section>

</body>
</html>
```